A wordpress website for the coolest Resort App

We have developed a mobile app - Zorbo and we want to develop a cool, neat and simple wordpress website for it.

I have attached the basics in a keynote/ ppt - but i need you to bring it more to life. plus there are additions:

FOr the number of pages, we will have:
1- Home: very similar to the one pager
2- How it works: Showing step by step on how the app works, and how it connects to the POS system of the restaurant etc with spanshots from the app
3- Benefit: Elaborating more on each of the benefits that is mentioned in the ONE PAGE document, with additional statistics, reference etc.. and embedded videos and animation
4- who we are page
5- In the press page: links to the articles where zorbo was mentioned
6- Get in touch page
7- FAQ
Updates

Target Market(s)

Resorts, hotels, beach and pool restaurant operators

Industry/Entity Type

Hospitality

Coding

Coded - Design and coding required

Font styles to use
Other font styles liked:
• I have attached the fonts i want to use: ROboto is the main font

Colors

Designer to choose colors to be used in the design.

Requirements
Must have
• Logo, icons for each benefit, you can also use the mood picture i attached or any other picture you recommend - maybe just something related to the app
• I also attached the Main colour, the orange and the blue is the accent one
• I attached the fonts, roboto is the main one
• there should also be a contact us:
• Email : info@zorboapp-mail.com
• Mobile: +971 5 23 47 90 18
• Address: Palm Quarter - Dubai - United Arab Emirates

```html
<!DOCTYPE html>
<html lang="en">
<head>
<meta charset="utf-8">
<title>Zorbo – Smart Resort Ordering App</title>
<link href="https://fonts.googleapis.com/css2?family=Roboto:wght@300;400;500;700&display=swap" rel="stylesheet">
<style>
:root{
  --orange:#f47b48;
  --orange-soft:#f9a47f;
  --blue:#2e9bd3;
  --blue-dark:#1f84bb;
  --ink:#333333;
  --text:#6f6f6f;
  --muted:#9a9a9a;
  --line:#e3e3e3;
  --paper:#ffffff;
  --soft:#f5f5f5;
  --footer:#383838;
}
*{box-sizing:border-box;margin:0;padding:0}
html,body{width:1200px;height:4317px;overflow:hidden}
body{font-family:'Roboto',sans-serif;color:var(--text);background:var(--paper);position:relative}
.section{position:absolute;left:0;width:1200px}
.abs{position:absolute}
.title{font-weight:700;font-size:25px;color:var(--orange);letter-spacing:.5px;text-transform:uppercase}
.title.center{width:100%;text-align:center}
.lede{width:100%;text-align:center;font-size:12px;color:var(--text)}
.copy{font-size:12.5px;line-height:22px;color:var(--text)}

/* header */
.site-header{top:0;height:100px;background:var(--paper)}
.brand{left:86px;top:28px;display:flex;align-items:center;gap:10px}
.brand-dot{width:30px;height:30px;border-radius:50%;background:var(--orange)}
.brand-name{font-weight:700;font-size:34px;color:var(--ink);line-height:1}
.nav{right:40px;top:36px;display:flex;gap:40px;font-size:12px;font-weight:500;color:var(--ink);text-transform:uppercase}
.nav .active{color:var(--orange)}

/* hero */
.hero{top:100px;height:576px;background:linear-gradient(180deg,#8fc6e6 0%,#b8dcef 30%,#3aa6c4 48%,#5ec1cf 58%,#e8dcc6 74%,#d9c6a4 100%)}
.hero-arrow{top:236px;width:40px;height:40px;border-radius:50%;border:2px solid #fff;display:flex;align-items:center;justify-content:center}

/* how it works */
.how{top:676px;height:532px;background:var(--paper)}
.phone-outline{left:808px;top:-16px;width:200px;height:310px;border:3px solid #cfcfcf;border-radius:28px;background:#fff}
.phone-outline .screen{position:absolute;left:12px;right:12px;top:40px;bottom:46px;border:1px solid #e2e2e2;display:flex;align-items:center;justify-content:center;font-weight:700;font-size:30px;color:var(--orange)}
.phone-outline .speaker{position:absolute;left:80px;top:18px;width:40px;height:5px;border-radius:3px;background:#ddd}
.phone-outline .home-btn{position:absolute;left:84px;bottom:10px;width:28px;height:28px;border-radius:50%;border:2px solid #ddd}
.step{top:333px;width:180px;text-align:center}
.step-circle{width:110px;height:110px;border-radius:50%;background:var(--orange);margin:0 auto;display:flex;align-items:center;justify-content:center}
.step-label{margin-top:18px;font-size:13px;font-weight:700;color:var(--ink);text-transform:uppercase;line-height:18px}
.dots{top:380px}

/* benefit */
.benefit{top:1208px;height:1085px;background:var(--paper);border-top:1px solid var(--line)}
.sub-head{width:100%;text-align:center;font-size:13px;font-weight:700;color:var(--blue);text-transform:uppercase}
.feature-name{font-size:16px;font-weight:700;color:var(--blue);text-transform:uppercase}
.feature-text{font-size:11.5px;line-height:20px;color:var(--text)}
.badge{width:46px;height:46px;border-radius:8px;background:#fff;border:2px solid var(--blue);display:flex;align-items:center;justify-content:center}
.resort-card{width:478px;height:64px;border:1.5px solid var(--orange-soft);border-radius:6px;background:#fff}
.resort-card .icon{position:absolute;left:14px;top:8px;width:46px;height:46px;border-radius:50%;border:1.5px solid var(--orange);display:flex;align-items:center;justify-content:center}
.resort-card p{position:absolute;left:96px;right:20px;top:11px;font-size:11.5px;line-height:21px;color:var(--text)}

/* who we are */
.who{top:2293px;height:325px;background:var(--blue)}
.who .title{color:#fff}
.who .copy{color:#e8f4fb}
.phone-white{left:835px;top:10px;width:130px;height:300px;border-radius:22px;background:#fdfdfd;box-shadow:0 4px 14px rgba(0,0,0,.18)}
.phone-white .screen{position:absolute;left:8px;right:8px;top:34px;bottom:38px;background:#fff;border:1px solid #eee;display:flex;align-items:center;justify-content:center;font-weight:700;font-size:22px;color:var(--orange)}

/* press */
.press{top:2618px;height:575px;background:var(--paper)}
.card{top:144px;width:337px}
.card-img{width:337px;height:210px}
.card h3{margin-top:34px;font-size:13px;font-weight:700;color:var(--ink);text-transform:uppercase}
.card .meta{margin-top:16px;padding:6px 0;border-top:1px solid var(--line);border-bottom:1px solid var(--line);font-size:9px;color:var(--muted);display:flex;gap:22px}
.card p{margin-top:12px;font-size:11px;line-height:19px;color:var(--text)}

/* contact */
.contact{top:3193px;height:317px;background:var(--paper);border-top:1px solid var(--line)}
.field{height:40px;border:1px solid var(--line);background:#fff;font-size:11px;color:var(--muted);padding:12px 14px}
.submit{height:40px;background:var(--orange);color:#fff;font-size:12px;font-weight:700;text-align:center;line-height:40px;text-transform:uppercase}

/* faq */
.faq{top:3510px;height:489px;background:var(--soft)}
.faq-item{width:478px;background:#fff;border:1px solid var(--line)}
.faq-q{height:44px;padding:0 18px;display:flex;align-items:center;justify-content:space-between;font-size:12px;font-weight:500;color:var(--ink)}
.faq-toggle{width:14px;height:14px;border-radius:50%;background:#bdbdbd;position:relative}
.faq-toggle::before,.faq-toggle::after{content:"";position:absolute;background:#fff;left:3px;top:6px;width:8px;height:2px}
.faq-toggle::after{transform:rotate(90deg)}
.faq-a{padding:4px 18px 16px;font-size:11px;line-height:19px;color:var(--text);border-top:1px solid var(--line)}

/* footer */
.footer{top:3999px;height:318px;background:var(--footer);color:#ddd}
.footer-brand{left:110px;top:118px;display:flex;align-items:center;gap:14px}
.footer-brand .brand-dot{width:54px;height:54px}
.footer-brand .brand-name{font-size:60px;color:#fff}
.footer h4{font-size:15px;font-weight:700;color:#fff;text-transform:uppercase;letter-spacing:.5px}
.footer-list{list-style:none;font-size:11px;line-height:20px;color:#d6d6d6}
.footer-list li{display:flex;gap:10px;align-items:flex-start;margin-bottom:8px}
.footer-list svg{flex:none;margin-top:4px}
.email-field{width:198px;height:32px;background:#fff;font-size:10px;color:var(--muted);padding:10px}
.subscribe{width:74px;height:22px;background:var(--orange);color:#fff;font-size:9px;font-weight:700;text-align:center;line-height:22px;text-transform:uppercase}
.social{display:flex;gap:8px}
.social span{width:34px;height:34px;border-radius:50%;border:1.5px solid #fff;display:block}
.copyright{top:272px;width:100%;text-align:center;font-size:10px;color:#cfcfcf}
</style>
</head>
<body>

<header class="section site-header">
  <div class="abs brand"><span class="brand-dot"></span><span class="brand-name">zorbo</span></div>
  <nav class="abs nav">
    <span class="active">Home</span><span>How it works</span><span>Benefit</span><span>Who we are</span><span>Press</span><span>Get in touch</span><span>FAQ</span>
  </nav>
</header>

<section class="section hero" role="img" aria-label="Couple relaxing in striped beach chairs on a tropical beach, toasting with cocktails">
  <div class="abs hero-arrow" style="left:32px"><svg width="12" height="14" viewBox="0 0 12 14"><path d="M9 1 3 7l6 6" fill="none" stroke="#fff" stroke-width="2"/></svg></div>
  <div class="abs hero-arrow" style="right:32px"><svg width="12" height="14" viewBox="0 0 12 14"><path d="M3 1l6 6-6 6" fill="none" stroke="#fff" stroke-width="2"/></svg></div>
</section>

<section class="section how">
  <h2 class="abs title" style="left:86px;top:4px">How it works</h2>
  <p class="abs copy" style="left:86px;top:48px;width:610px">Zorbo is a smart mobile app that the resort guests download it on their mobile. Through this app, the user locates himself and then can. The resort receives the app requests on a dedicated POS, to ensure a seamless manage ment of operation. The POS provides details of the requests and a summary of the daily activity and controls other aspect of the operation.</p>
  <p class="abs copy" style="left:86px;top:156px;width:610px">Sed ut perspiciatis unde omnis iste natus error sit voluptatem accusantium doloremque laudanti um, totam rem aperiam, eaque ipsa quae ab illo inventore veritatis et quasi architecto beatae vitae dicta sunt explicabo. Nemo enim ipsam voluptatem quia voluptas sit aspernatur.</p>
  <div class="abs phone-outline"><span class="speaker"></span><div class="screen">zorbo</div><span class="home-btn"></span></div>

  <svg class="abs dots" style="left:0" width="1200" height="30" viewBox="0 0 1200 30">
    <g fill="none" stroke="#bbb" stroke-width="1.5" stroke-dasharray="3 4">
      <path d="M232 14 Q276 2 318 14"/><path d="M459 14 Q500 2 540 14"/><path d="M664 14 Q710 2 756 14"/><path d="M897 14 Q930 2 966 14"/>
    </g>
    <g fill="#bbb"><path d="M318 14l-7-5 1 8z"/><path d="M540 14l-7-5 1 8z"/><path d="M756 14l-7-5 1 8z"/><path d="M966 14l-7-5 1 8z"/></g>
  </svg>

  <div class="abs step" style="left:74px">
    <div class="step-circle"><svg width="44" height="36" viewBox="0 0 44 36"><g stroke="#fff" stroke-width="5" stroke-linecap="round"><path d="M4 5h36M4 18h36M4 31h36"/></g></svg></div>
    <div class="step-label">Check the menu</div>
  </div>
  <div class="abs step" style="left:301px">
    <div class="step-circle"><svg width="50" height="50" viewBox="0 0 50 50" fill="none" stroke="#fff" stroke-width="2.5"><circle cx="25" cy="27" r="17"/><circle cx="25" cy="27" r="10"/><path d="M7 6v14M4 6v8h6V6M43 6v36M43 6c-4 2-5 8-5 12h5"/></svg></div>
    <div class="step-label">Order the food &amp;<br>drinks</div>
  </div>
  <div class="abs step" style="left:506px">
    <div class="step-circle"><svg width="54" height="50" viewBox="0 0 54 50" fill="none" stroke="#fff" stroke-width="2.5"><path d="M10 34a17 17 0 0 1 34 0z"/><path d="M6 38h42"/><circle cx="27" cy="14" r="3"/><path d="M27 4v4"/></svg></div>
    <div class="step-label">Call the waiter</div>
  </div>
  <div class="abs step" style="left:739px">
    <div class="step-circle"><svg width="50" height="46" viewBox="0 0 50 46"><path d="M4 22 46 4 36 42 24 30z" fill="#fff"/><path d="M24 30 46 4 18 26v14z" fill="#ffd8c6"/></svg></div>
    <div class="step-label">Send requests to<br>the waiter</div>
  </div>
  <div class="abs step" style="left:940px">
    <div class="step-circle"><svg width="54" height="44" viewBox="0 0 54 44" fill="none" stroke="#fff" stroke-width="2.5"><rect x="4" y="6" width="40" height="26" rx="3"/><path d="M4 14h40"/><rect x="14" y="16" width="36" height="22" rx="3" fill="#f47b48"/><path d="M20 30h10"/></svg></div>
    <div class="step-label">Checkout and pay</div>
  </div>
</section>

<section class="section benefit">
  <h2 class="abs title center" style="top:48px">Our benefit</h2>
  <p class="abs lede" style="top:96px">Sed ut perspiciatis unde omnis iste natus error sit voluptatem accusantium doloremque laudantium, totam rem aperiam, eaque ipsa</p>
  <h3 class="abs sub-head" style="top:160px">The benefits for the guests</h3>

  <svg class="abs" style="left:458px;top:212px" width="284" height="284" viewBox="0 0 284 284"><circle cx="142" cy="142" r="128" fill="none" stroke="var(--blue)" stroke-width="3"/></svg>
  <div class="abs" style="left:555px;top:275px;width:90px;height:158px;border:2px solid #cfcfcf;border-radius:12px;background:#fff">
    <div style="position:absolute;left:6px;right:6px;top:18px;bottom:20px;border:1px solid #e2e2e2;display:flex;align-items:center;justify-content:center;font-weight:700;font-size:15px;color:var(--orange)">zorbo</div>
  </div>
  <div class="abs badge" style="left:478px;top:236px"><svg width="26" height="26" viewBox="0 0 26 26" fill="none" stroke="var(--blue)" stroke-width="2"><rect x="3" y="3" width="20" height="20" rx="2"/><path d="M13 3v20M6 8h4M6 12h4M16 8h4M16 12h4"/></svg></div>
  <div class="abs badge" style="left:676px;top:236px"><svg width="26" height="26" viewBox="0 0 26 26" fill="none" stroke="var(--blue)" stroke-width="2.2"><path d="M4 22 16 10M18 4l4 4-4 4-4-4zM4 4l18 18"/></svg></div>
  <div class="abs badge" style="left:478px;top:418px"><svg width="26" height="26" viewBox="0 0 26 26" fill="none" stroke="var(--blue)" stroke-width="2"><circle cx="13" cy="14" r="9"/><path d="M13 14l4-4M10 3h6"/></svg></div>
  <div class="abs badge" style="left:676px;top:418px"><svg width="26" height="26" viewBox="0 0 26 26" fill="none" stroke="var(--blue)" stroke-width="2"><path d="M3 5h4l3 12h11l2-8H8"/><circle cx="11" cy="21" r="2"/><circle cx="19" cy="21" r="2"/></svg></div>

  <div class="abs" style="left:140px;top:230px;width:300px;text-align:right">
    <div class="feature-name">Menu</div>
    <p class="feature-text" style="margin-top:8px">see a visual for each item, and have all relevant dietary details provided to them – including allergens</p>
  </div>
  <div class="abs" style="left:762px;top:230px;width:300px">
    <div class="feature-name">Customization</div>
    <p class="feature-text" style="margin-top:8px">customize the order and avoid human error</p>
  </div>
  <div class="abs" style="left:140px;top:402px;width:300px;text-align:right">
    <div class="feature-name">Speed</div>
    <p class="feature-text" style="margin-top:8px">No more time lost catching a waiter - Submit your orders/requests and lay back</p>
  </div>
  <div class="abs" style="left:762px;top:402px;width:300px">
    <div class="feature-name">Fast checkout</div>
    <p class="feature-text" style="margin-top:8px">Avoid waiting for the bill, use the saved credit card, or pay cash</p>
  </div>

  <h3 class="abs sub-head" style="top:568px">The benefits for the resort</h3>

  <div class="abs resort-card" style="left:86px;top:636px"><span class="icon"><svg width="24" height="24" viewBox="0 0 24 24" fill="none" stroke="var(--orange)" stroke-width="2"><circle cx="12" cy="13" r="8"/><path d="M12 9v4l3 2M4 4l3-2M20 4l-3-2"/></svg></span><p>Increase your speed of service by up to 50% by savings on all the inefficient waiter's runs back and forth between the guests</p></div>
  <div class="abs resort-card" style="left:636px;top:636px"><span class="icon"><svg width="24" height="24" viewBox="0 0 24 24" fill="none" stroke="var(--orange)" stroke-width="2"><rect x="5" y="4" width="14" height="17" rx="1"/><path d="M9 3h6v3H9zM8 11h8M8 15h8"/></svg></span><p>Know more about the profile of your customers and optimize your offers to them accordingly</p></div>
  <div class="abs resort-card" style="left:86px;top:742px"><span class="icon"><svg width="24" height="24" viewBox="0 0 24 24" fill="none" stroke="var(--orange)" stroke-width="2"><path d="M7 9h10l2 11H5zM9 9l-2-5h10l-2 5M12 12v5"/></svg></span><p>Optimize up to 70% of your waiters' costs with Zorbo – Save it or redeploy it where it matters</p></div>
  <div class="abs resort-card" style="left:636px;top:742px"><span class="icon"><svg width="24" height="24" viewBox="0 0 24 24" fill="none" stroke="var(--orange)" stroke-width="2"><circle cx="15" cy="4" r="2"/><path d="M6 10l5-3 3 4 5 1M11 7l-2 7 4 3-2 5M9 14l-5 3"/></svg></span><p>Apply your menu changes seamlessly on the spot, avoid reprinting costs !</p></div>
  <div class="abs resort-card" style="left:86px;top:849px"><span class="icon"><svg width="24" height="24" viewBox="0 0 24 24" fill="none" stroke="var(--orange)" stroke-width="2"><rect x="4" y="3" width="13" height="18" rx="1"/><path d="M7 8h7M7 12h7M7 16h4M20 6l-6 10"/></svg></span><p>Eliminate human error when taking the order's notes and get the order delivered exactly as requested</p></div>
  <div class="abs resort-card" style="left:636px;top:849px"><span class="icon"><svg width="24" height="24" viewBox="0 0 24 24" fill="none" stroke="var(--orange)" stroke-width="2"><path d="M3 10v4h4l9 5V5L7 10zM19 9v6M7 14l2 6"/></svg></span><p>Use Zorbo as a platform to build a loyalty scheme, and make sure you keep your loyal customers</p></div>
  <div class="abs resort-card" style="left:86px;top:955px"><span class="icon"><svg width="24" height="24" viewBox="0 0 24 24" fill="none" stroke="var(--orange)" stroke-width="2"><path d="M4 20h16M6 20v-5M10 20v-9M14 20v-6M18 20V5"/></svg></span><p>Increase your average check value by more than 20% through the carefully designed in app tactics of up and cross selling</p></div>
  <div class="abs resort-card" style="left:636px;top:955px"><span class="icon"><svg width="24" height="24" viewBox="0 0 24 24" fill="none" stroke="var(--orange)" stroke-width="2"><path d="M12 3a6 6 0 0 1 4 10.5V17H8v-3.5A6 6 0 0 1 12 3zM9 20h6"/></svg></span><p>Use Zorbo as a platform to run surveys, with a higher completion rate</p></div>
</section>

<section class="section who">
  <h2 class="abs title" style="left:86px;top:48px">Who we are</h2>
  <p class="abs copy" style="left:86px;top:92px;width:680px">Zorbo is a smart mobile app that the resort guests download it on their mobile. Through this app, the user locates himself and then can. The resort receives the app requests on a dedicated POS, to ensure a seamless manage ment of operation. The POS provides details of the requests and a summary of the daily activity and controls other aspect of the operation.</p>
  <p class="abs copy" style="left:86px;top:206px;width:680px">Sed ut perspiciatis unde omnis iste natus error sit voluptatem accusantium doloremque laudanti um, totam rem aperiam, eaque ipsa quae ab illo inventore veritatis et quasi architecto beatae vitae dicta sunt explicabo. Nemo enim ipsam voluptatem quia voluptas sit aspernatur.</p>
  <div class="abs phone-white"><div class="screen">zorbo</div></div>
</section>

<section class="section press">
  <h2 class="abs title center" style="top:60px">In the press</h2>
  <p class="abs lede" style="top:100px">Sed ut perspiciatis unde omnis iste natus error sit voluptatem accusantium doloremque laudantium, totam rem aperiam, eaque ipsa</p>

  <article class="abs card" style="left:86px">
    <div class="card-img" role="img" aria-label="Smiling woman using a tablet" style="background:linear-gradient(135deg,#e9e4df,#cfc3b8 60%,#f2efec)"></div>
    <h3>Sed ut perspiciatis..</h3>
    <div class="meta"><span>27 MARCH 2017</span><span>123</span><span>LIKE</span><span>SHARE</span></div>
    <p>Sed ut perspiciatis unde omnis iste natus error sit volupta tem accusantium doloremque laudantium, totam rem aper architecto beatae vitae dicta sunt explicabo.</p>
  </article>
  <article class="abs card" style="left:437px">
    <div class="card-img" role="img" aria-label="Waitress serving guests at a busy restaurant" style="background:linear-gradient(135deg,#7a6a5a,#b9a996 55%,#d8cfc3)"></div>
    <h3>Sed ut perspiciatis..</h3>
    <div class="meta"><span>27 MARCH 2017</span><span>123</span><span>LIKE</span><span>SHARE</span></div>
    <p>Sed ut perspiciatis unde omnis iste natus error sit volupta tem accusantium doloremque laudantium, totam rem aper architecto beatae vitae dicta sunt explicabo.</p>
  </article>
  <article class="abs card" style="left:779px">
    <div class="card-img" role="img" aria-label="Hands holding a tablet at a café table with coffee" style="background:linear-gradient(135deg,#c9b8a4,#e6ddd2 50%,#8f6f55)"></div>
    <h3>Sed ut perspiciatis..</h3>
    <div class="meta"><span>27 MARCH 2017</span><span>123</span><span>LIKE</span><span>SHARE</span></div>
    <p>Sed ut perspiciatis unde omnis iste natus error sit volupta tem accusantium doloremque laudantium, totam rem aper architecto beatae vitae dicta sunt explicabo.</p>
  </article>
</section>

<section class="section contact">
  <h2 class="abs title center" style="top:38px">Get in touch</h2>
  <p class="abs lede" style="top:78px">Sed ut perspiciatis unde omnis iste natus error sit voluptatem accusantium doloremque laudantium, totam rem aperiam, eaque ipsa</p>
  <div class="abs field" style="left:300px;top:124px;width:290px">Name</div>
  <div class="abs field" style="left:300px;top:173px;width:290px">Email</div>
  <div class="abs field" style="left:300px;top:222px;width:290px">Phone</div>
  <div class="abs field" style="left:607px;top:124px;width:293px;height:89px">Message</div>
  <div class="abs submit" style="left:607px;top:222px;width:293px">Submit</div>
</section>

<section class="section faq">
  <h2 class="abs title center" style="top:36px">FAQ's</h2>
  <p class="abs lede" style="top:76px">Sed ut perspiciatis unde omnis iste natus error sit voluptatem accusantium doloremque laudantium, totam rem aperiam, eaque ipsa</p>

  <div class="abs faq-item" style="left:86px;top:126px">
    <div class="faq-q">Sed ut perspiciatis unde omnis iste natus<span class="faq-toggle"></span></div>
    <div class="faq-a">Nemo enim ipsam voluptatem quia voluptas sit aspernatur aut odit aut fugit, sed quia consequuntur magni dolores eos qui ratione voluptatem sequi nesciunt. Neque porro quisquam est, qui dolorem ipsum quia dolor sit amet.</div>
  </div>
  <div class="abs faq-item" style="left:636px;top:126px">
    <div class="faq-q">Sed ut perspiciatis unde omnis iste natus<span class="faq-toggle"></span></div>
    <div class="faq-a">Nemo enim ipsam voluptatem quia voluptas sit aspernatur aut odit aut fugit, sed quia consequuntur magni dolores eos qui ratione voluptatem sequi nesciunt. Neque porro quisquam est, qui dolorem ipsum quia dolor sit amet.</div>
  </div>
  <div class="abs faq-item" style="left:86px;top:298px"><div class="faq-q">Sed ut perspiciatis unde omnis iste natus<span class="faq-toggle"></span></div></div>
  <div class="abs faq-item" style="left:636px;top:298px"><div class="faq-q">Sed ut perspiciatis unde omnis iste natus<span class="faq-toggle"></span></div></div>
  <div class="abs faq-item" style="left:86px;top:353px"><div class="faq-q">Sed ut perspiciatis unde omnis iste natus<span class="faq-toggle"></span></div></div>
  <div class="abs faq-item" style="left:636px;top:353px"><div class="faq-q">Sed ut perspiciatis unde omnis iste natus<span class="faq-toggle"></span></div></div>
  <div class="abs faq-item" style="left:86px;top:408px"><div class="faq-q">Sed ut perspiciatis unde omnis iste natus<span class="faq-toggle"></span></div></div>
  <div class="abs faq-item" style="left:636px;top:408px"><div class="faq-q">Sed ut perspiciatis unde omnis iste natus<span class="faq-toggle"></span></div></div>
</section>

<footer class="section footer">
  <div class="abs footer-brand"><span class="brand-dot"></span><span class="brand-name">zorbo</span></div>

  <div class="abs" style="left:403px;top:50px;width:220px">
    <h4>Contact us</h4>
    <ul class="footer-list" style="margin-top:16px">
      <li><svg width="10" height="12" viewBox="0 0 10 12"><path d="M2 1h6v10H2z" fill="none" stroke="#fff" stroke-width="1.4"/></svg>+971 5 23 47 90 18 (Phone)</li>
      <li><svg width="10" height="12" viewBox="0 0 10 12"><path d="M2 1h6v10H2z" fill="none" stroke="#fff" stroke-width="1.4"/></svg>+971 5 23 47 90 18 (Fax)</li>
      <li><svg width="12" height="10" viewBox="0 0 12 10"><path d="M1 1h10v8H1zM1 1l5 4 5-4" fill="none" stroke="#fff" stroke-width="1.3"/></svg><span style="text-decoration:underline">info@zorboapp-mail.com</span></li>
      <li><svg width="10" height="13" viewBox="0 0 10 13"><path d="M5 12S1 7 1 5a4 4 0 0 1 8 0c0 2-4 7-4 7z" fill="#fff"/><circle cx="5" cy="5" r="1.5" fill="#383838"/></svg>Palm Quarter - Dubai - United Arab<br>Emirates</li>
    </ul>
  </div>

  <div class="abs" style="left:662px;top:50px;width:220px">
    <h4>Stay in the loop.</h4>
    <p style="margin-top:16px;font-size:11px;line-height:18px;color:#d6d6d6">Register Your email address to get information about us.</p>
    <div class="email-field" style="margin-top:14px">Email Address</div>
    <div class="subscribe" style="margin-top:10px">Subscribe</div>
  </div>

  <div class="abs" style="left:906px;top:50px;width:220px">
    <h4>Follow us</h4>
    <p style="margin-top:16px;font-size:11px;line-height:18px;color:#d6d6d6">Lorem ipsum dolor sit amet, conse ctetur adipiscing elit. Nulla in purus nibh. Donec ornare</p>
    <div class="social" style="margin-top:14px"><span></span><span></span><span></span><span></span><span></span><span></span></div>
  </div>

  <p class="abs copyright">© Copyright 2017 Zorbo AM All Rights Reserved</p>
</footer>

</body>
</html>
```